BrightNomadRx.com Blog Design (Travel, Lifestyle, and Life Hacking blog)

I am launching a lifestyle blog about my life. I'm a doctor who travels the world trying the best restaurants, airlines and trying to have as much fun as possible. I also invest in startups, and am always trying new tricks to make life better. I also plan to write about various other topics, but essentially it is about travel, lifestyle and medicine. I need a creative and really awesome looking design for a new wordpress blog called BrightNomadRx

Target Market(s)

Physicians, Entrepreneurs, Travellers

Industry/Entity Type

Airlines

Number of Pages Required

1 page

Font styles to use
Serif

Requirements
Must have
• Slick looking graphics with a highly professional modern feel

```html
<!DOCTYPE html>
<html lang="en">
<head>
<meta charset="utf-8">
<title>Bright Nomad Rx — Blog</title>
<link rel="stylesheet" href="https://fonts.googleapis.com/css2?family=Raleway:wght@400;500;600;700&family=Oswald:wght@300&family=Arimo:wght@400&display=swap">
<style>
:root{
  --ink:#222222;
  --dark:#2b2b2b;
  --text:#555555;
  --muted:#666666;
  --accent:#0aa7e8;
  --page:#f7f7f7;
  --rule:#dddddd;
  --white:#ffffff;
}
*{box-sizing:border-box;margin:0;padding:0}
html,body{width:1162px;height:1200px;overflow:hidden}
body{position:relative;background:var(--page);font-family:"Raleway",sans-serif;color:var(--ink)}

.site-header{position:absolute;left:0;top:0;width:1162px;height:75px;background:var(--dark)}
.brand{position:absolute;left:68px;top:34px;color:var(--white);font:700 24px "Raleway",sans-serif}
.brand::before{content:"";position:absolute;left:-2px;top:-14px;width:145px;height:2px;background:var(--white);border-radius:2px}
.nav{position:absolute;left:385px;top:0;display:flex;height:75px}
.nav a{display:flex;align-items:center;height:75px;color:var(--white);text-decoration:none;font:400 17px "Raleway",sans-serif;padding:0 28px 0 0}
.nav a.active{background:var(--accent);padding:0 15px;margin-right:40px}
.social{position:absolute;left:994px;top:25px;display:flex;gap:8px}
.social span{width:21px;height:21px;border:1.5px solid var(--accent)}

.post{position:absolute;left:60px;width:754px;height:190px}
.post-meta{position:absolute;left:3px;top:0;width:120px}
.day{font:300 56px/1 "Oswald",sans-serif;color:var(--ink)}
.month{font:500 20px "Raleway",sans-serif;margin-top:2px}
.meta-label{font:400 12.5px "Raleway",sans-serif;color:var(--ink);margin-top:18px;line-height:16px}
.meta-value{font:600 12.5px "Raleway",sans-serif;line-height:16px}
.post-image{position:absolute;left:130px;top:0;width:234px;height:183px}
.post-body{position:absolute;left:404px;top:3px;width:350px}
.post-title{font:600 20px "Raleway",sans-serif;color:var(--ink)}
.post-excerpt{font:400 13px/20.5px "Arimo",sans-serif;color:var(--text);margin-top:14px}
.read-more{display:inline-block;margin-top:13px;font:500 15.5px "Raleway",sans-serif;color:var(--accent);text-decoration:none}
.divider{position:absolute;left:60px;width:754px;height:1px;background:var(--rule)}

.load-more{position:absolute;left:352px;top:1134px;display:flex;align-items:center;gap:9px;font:400 13.5px "Raleway",sans-serif;color:var(--muted)}

.sidebar{position:absolute;left:844px;top:0;width:260px}
.widget{position:absolute;left:0;width:260px}
.widget-title{font:600 19px "Raleway",sans-serif;color:var(--ink);padding-left:2px;padding-bottom:6px;border-bottom:1px solid var(--rule)}
.recent li{list-style:none;font:400 13.5px "Arimo",sans-serif;color:var(--text);line-height:26px;padding-left:1px}
.search{display:flex;height:36px}
.search span{flex:1;background:var(--white)}
.search b{width:79px;background:var(--accent);color:var(--white);font:700 18px/36px "Raleway",sans-serif;text-align:center}
.tags{display:flex;flex-wrap:wrap;gap:8px 8px;margin-top:12px}
.tags span{background:var(--dark);color:var(--white);font:400 13.5px/27px "Raleway",sans-serif;padding:0 8px}
.cats li{list-style:none;display:flex;align-items:center;gap:6px;font:400 15.5px/24.5px "Raleway",sans-serif;color:var(--ink);padding-left:2px}
.weather{margin-top:0;height:183px;background:var(--dark);color:var(--white);position:relative}
.wx-head{position:absolute;left:12px;top:9px;font:400 16px "Raleway",sans-serif}
.wx-head em{font-style:normal;margin-left:8px}
.wx-next{position:absolute;right:6px;top:9px}
.wx-place{position:absolute;left:26px;top:58px;font:500 13px "Raleway",sans-serif}
.wx-big{position:absolute;left:12px;top:75px}
.wx-temp{position:absolute;left:9px;top:142px;font:700 15px "Raleway",sans-serif}
.wx-split{position:absolute;left:79px;top:53px;width:1px;height:122px;background:var(--white)}
.wx-row{position:absolute;left:100px;display:flex;align-items:center;gap:12px;font:500 12.5px "Raleway",sans-serif;letter-spacing:.2px}
.news-text{font:400 13.5px/21px "Arimo",sans-serif;color:var(--text);margin-top:4px}
.signup{display:flex;height:37px;margin-top:12px;border:1px solid var(--rule)}
.signup span{flex:1;background:var(--white);font:400 13.5px/35px "Arimo",sans-serif;padding-left:9px}
.signup b{width:75px;background:var(--accent);color:var(--white);font:400 17px/35px "Raleway",sans-serif;text-align:center}
.rule{position:absolute;left:0;width:260px;height:1px;background:var(--rule)}

.site-footer{position:absolute;left:0;top:1171px;width:1162px;height:29px;background:var(--dark);color:var(--white);font:500 12px/29px "Raleway",sans-serif;text-align:center}
</style>
</head>
<body>
<header class="site-header">
  <div class="brand">Bright Nomad Rx</div>
  <nav class="nav">
    <a class="active">Blog</a><a>Pictures</a><a>About Me</a><a>Contact Me</a>
  </nav>
  <div class="social"><span></span><span></span><span></span><span></span></div>
</header>

<article class="post" style="top:113px">
  <div class="post-meta">
    <div class="day">28</div><div class="month">DEC 2016</div>
    <div class="meta-label">Posted By</div><div class="meta-value">Admin</div>
    <div class="meta-label">Category</div><div class="meta-value">Travel</div>
  </div>
  <div class="post-image" role="img" aria-label="Wooden pier over turquoise sea under a blue sky" style="background:linear-gradient(180deg,#4fa6e0 0%,#a9d8f2 40%,#27c7d8 60%,#b58a5a 100%)"></div>
  <div class="post-body">
    <h2 class="post-title">LOREM IPSUM DOLOR!</h2>
    <p class="post-excerpt">Lorem ipsum dolor sit amet, consectetuer adipiscingelit, sed diam nonummy nibh euismod tincidunt ut laoreet dol magna Lorem ipsum dolor sit amet, consectetuer adipiscinglit, sed diam nonummy nibh</p>
    <a class="read-more">READ MORE</a>
  </div>
</article>
<div class="divider" style="top:338px"></div>

<article class="post" style="top:379px">
  <div class="post-meta">
    <div class="day">01</div><div class="month">JAN 2017</div>
    <div class="meta-label">Posted By</div><div class="meta-value">Admin</div>
    <div class="meta-label">Category</div><div class="meta-value">Lifestyle</div>
  </div>
  <div class="post-image" role="img" aria-label="Hiker with raised arms on a rock overlooking green valley at sunrise" style="background:linear-gradient(180deg,#9fc3d6 0%,#e9e27a 40%,#6f9a3c 70%,#8a7a5e 100%)"></div>
  <div class="post-body">
    <h2 class="post-title">LOREM IPSUM DOLOR!</h2>
    <p class="post-excerpt">Lorem ipsum dolor sit amet, consectetuer adipiscing elit, sed diam nonummy nibh euismod tincidunt ut laoreet dolore magna Lorem ipsum dolor sit amet, consectetuer adipiscing elit, sed diam nonummy nibh</p>
    <a class="read-more">READ MORE</a>
  </div>
</article>
<div class="divider" style="top:605px"></div>

<article class="post" style="top:643px">
  <div class="post-meta">
    <div class="day">05</div><div class="month">JAN 2017</div>
    <div class="meta-label">Posted By</div><div class="meta-value">Admin</div>
    <div class="meta-label">Category</div><div class="meta-value">Medicine</div>
  </div>
  <div class="post-image" role="img" aria-label="Team of medical staff in white coats" style="background:linear-gradient(135deg,#f2f4f6 0%,#dfe6ec 55%,#7fa8c8 100%)"></div>
  <div class="post-body">
    <h2 class="post-title">LOREM IPSUM DOLOR!</h2>
    <p class="post-excerpt">Lorem ipsum dolor sit amet, consectetuer adipiscing elit, sed diam nonummy nibh euismod tincidunt ut laoreet dolore magna Lorem ipsum dolor sit amet, consectetuer adipiscing elit, sed diam nonummy nibh</p>
    <a class="read-more">READ MORE</a>
  </div>
</article>
<div class="divider" style="top:868px"></div>

<article class="post" style="top:906px">
  <div class="post-meta">
    <div class="day">25</div><div class="month">JAN 2017</div>
    <div class="meta-label">posted by</div><div class="meta-value">admin</div>
    <div class="meta-label">category</div><div class="meta-value">Medicine</div>
  </div>
  <div class="post-image" role="img" aria-label="Hand touching a glowing blue medical interface screen" style="background:linear-gradient(135deg,#1d4f86 0%,#2f78b8 55%,#143a66 100%)"></div>
  <div class="post-body">
    <h2 class="post-title">LOREM IPSUM DOLOR!</h2>
    <p class="post-excerpt">Lorem ipsum dolor sit amet, consectetuer adipiscing elit, sed diam nonummy nibh euismod tincidunt ut laoreet dolore magna Lorem ipsum dolor sit amet, consectetuer adipiscing elit, sed diam nonummy nibh</p>
    <a class="read-more">READ MORE</a>
  </div>
</article>
<div class="divider" style="top:1120px"></div>

<div class="load-more">
  <svg width="19" height="19" viewBox="0 0 20 20" stroke="#999" stroke-width="2" stroke-linecap="round"><path d="M10 1v4M10 15v4M1 10h4M15 10h4M3.6 3.6l2.8 2.8M13.6 13.6l2.8 2.8M3.6 16.4l2.8-2.8M13.6 6.4l2.8-2.8"/></svg>
  <span>Load more blog</span>
</div>

<aside class="sidebar">
  <section class="widget" style="top:112px">
    <h3 class="widget-title">RECENT POSTS</h3>
    <ul class="recent" style="margin-top:4px">
      <li>Lorem ipsum dolor sit amet, consectetue</li>
      <li>Lorem ipsum dolor sit amet, consectetue</li>
      <li>Lorem ipsum dolor sit amet, consectetue</li>
      <li>Lorem ipsum dolor sit amet, consectetue</li>
    </ul>
  </section>
  <div class="rule" style="top:248px"></div>
  <div class="widget search" style="top:265px"><span></span><b>SEARCH</b></div>
  <div class="rule" style="top:318px"></div>

  <section class="widget" style="top:340px">
    <h3 class="widget-title">TAGS</h3>
    <div class="tags">
      <span>LOREM</span><span>LOREM IPSU</span><span>REM IPSU</span>
      <span style="padding:0 4px">LOREM IPSU</span><span style="padding:0 4px">REM IPSU</span><span>LORM DOL</span>
      <span style="padding:0 4px">LOREM IPSU</span><span style="padding:0 4px">REM IPSU</span><span>LOREM OL</span>
      <span style="padding:0 4px">LOREM IPSM DO</span><span>REM IPSU</span>
      <span>LOREM</span><span>LOREM IPSU</span><span>REM IPSU</span>
    </div>
  </section>
  <div class="rule" style="top:562px"></div>

  <section class="widget" style="top:582px">
    <h3 class="widget-title">CATEGORIES</h3>
    <ul class="cats" style="margin-top:4px">
      <li><svg width="16" height="16" viewBox="0 0 16 16"><path d="M2 9l4 5L14 2" fill="none" stroke="#0aa7e8" stroke-width="2.4" stroke-linecap="round"/></svg>LOREM</li>
      <li><svg width="16" height="16" viewBox="0 0 16 16"><path d="M2 9l4 5L14 2" fill="none" stroke="#0aa7e8" stroke-width="2.4" stroke-linecap="round"/></svg>LOREM IPSU</li>
      <li><svg width="16" height="16" viewBox="0 0 16 16"><path d="M2 9l4 5L14 2" fill="none" stroke="#0aa7e8" stroke-width="2.4" stroke-linecap="round"/></svg>REM IPSU</li>
      <li><svg width="16" height="16" viewBox="0 0 16 16"><path d="M2 9l4 5L14 2" fill="none" stroke="#0aa7e8" stroke-width="2.4" stroke-linecap="round"/></svg>REM IPSU</li>
    </ul>
  </section>
  <div class="rule" style="top:729px"></div>

  <section class="widget" style="top:747px">
    <h3 class="widget-title">WEATHER</h3>
  </section>
  <div class="widget weather" style="top:789px">
    <div class="wx-head">TODAY<em>07 January 2017</em></div>
    <svg class="wx-next" width="20" height="20" viewBox="0 0 20 20" fill="none" stroke="#fff" stroke-width="1.6"><circle cx="10" cy="10" r="8.5"/><path d="M5.5 10h8M10.5 6.5L14 10l-3.5 3.5"/></svg>
    <div class="wx-place">USA</div>
    <svg class="wx-big" width="52" height="52" viewBox="0 0 52 52"><g stroke="#fff" stroke-width="2.5" stroke-linecap="round"><path d="M24 3v6M24 43v6M3 24h6M8 8l4 4M40 8l-4 4M8 40l4-4"/></g><circle cx="24" cy="24" r="12" fill="none" stroke="#fff" stroke-width="3"/><path d="M22 40h22a6 6 0 0 0 0-12 9 9 0 0 0-17-2 7 7 0 0 0-5 14z" fill="#fff"/></svg>
    <div class="wx-temp">45°/14°</div>
    <div class="wx-split"></div>
    <div class="wx-row" style="top:59px"><svg width="26" height="26" viewBox="0 0 26 26" fill="none" stroke="#fff" stroke-width="1.5" stroke-linecap="round"><circle cx="13" cy="13" r="5"/><path d="M13 2v3M13 21v3M2 13h3M21 13h3M5 5l2 2M19 19l2 2M5 21l2-2M19 7l2-2"/></svg>MOSTLY SUNNY</div>
    <div class="wx-row" style="top:98px"><svg width="26" height="26" viewBox="0 0 26 26" fill="none" stroke="#fff" stroke-width="1.5"><path d="M13 3c4 6 7 9 7 13a7 7 0 0 1-14 0c0-4 3-7 7-13z"/></svg>HUMIDITY: 82°%</div>
    <div class="wx-row" style="top:137px"><svg width="26" height="26" viewBox="0 0 26 26" fill="none" stroke="#fff" stroke-width="1.5" stroke-linecap="round"><path d="M6 15h14a4 4 0 0 0-2-8 6 6 0 0 0-11 1 4 4 0 0 0-1 7zM8 19h12a2 2 0 1 1-2 2M4 22h9"/></svg>WIND: WAT 7 MPH</div>
  </div>
  <div class="rule" style="top:989px"></div>

  <section class="widget" style="top:1006px">
    <h3 class="widget-title">NEWSLETTER SIGNUP</h3>
    <p class="news-text">Lorm Ipsum Rem&nbsp; Rem Ipsu.Lorm Ipsum Rem&nbsp; Rem Ipsu.</p>
    <div class="signup"><span>E-mail</span><b>SUBMIT</b></div>
  </section>
</aside>

<footer class="site-footer">Copyright© 2017 Bright Nomad Rx. All rights reserved.</footer>
</body>
</html>
```